Autodetailing namecard design: Rose Gold Lettering on Black Matt

This is a namecard design project
requiring two-sided design
Base Color of Namecard: black matt

On front:
Company name,
"Lumina Finishes 14 Cendana"
Subtext: Auto Detailing Studio

Name of card holder: Marcus Oyelaran
Phone Number: +6011-4837-5062
address: 14, Jalan Cendana 5/3Taman Seri Cendana, 81400 Johor Bahru, Johor, Malaysia

Back:
Our Services
High Gloss Car Paint Protection
Custom Color Modification and Styling
Anti-Chip Glass Protection Film
Heat Rejection Glass Tinting

Target Market(s)

Autodetailing for highend cars

Contact Information for Business Card

as mentioned in project details

Colors

Designer to choose colors to be used in the design.

Requirements
Must have
• The main value-add to this project is the design of a logo suited for our purpose and name, and the inclusion of business card details into the card design

```html
<!DOCTYPE html>
<html lang="en">
<head>
<meta charset="UTF-8">
<title>Lumina Finishes 14 Cendana — Business Card</title>
<link rel="stylesheet" href="https://fonts.googleapis.com/css2?family=Bubblegum+Sans&family=Rubik:wght@700;800&family=Inter:wght@500&display=swap">
<style>
  :root {
    --stage: #141418;
    --card: #0a0a0b;
    --rose: #b4528e;
    --silver: #b4c0bc;
    --white: #ffffff;
  }
  * { margin: 0; padding: 0; box-sizing: border-box; }
  html, body { width: 1200px; height: 1200px; overflow: hidden; background: var(--stage); }
  .stage { position: relative; width: 1200px; height: 1200px; }
  .card {
    position: absolute; left: 193px; width: 814px; height: 481px;
    background: var(--card); overflow: hidden;
  }
  .card--front { top: 78px; }
  .card--back { top: 641px; }

  .brand-mark {
    position: absolute; left: 62px; top: 50px; width: 100px; height: 100px;
    background: var(--rose);
  }
  .brand-name {
    position: absolute; left: 238px; top: 40px;
    font-family: "Bubblegum Sans", cursive;
    font-size: 62px; line-height: 64px; color: var(--rose);
    text-transform: uppercase; white-space: nowrap;
  }
  .tagline {
    position: absolute; left: 250px; top: 177px;
    font-family: "Bubblegum Sans", cursive;
    font-size: 32px; color: var(--white); text-transform: uppercase; letter-spacing: 0.5px;
  }
  .holder {
    position: absolute; left: 46px; top: 228px;
    font-family: "Rubik", sans-serif; font-weight: 800; color: var(--white);
  }
  .holder__name { font-size: 28px; line-height: 32px; text-transform: uppercase; }
  .holder__phone { font-size: 28px; line-height: 32px; display: flex; align-items: center; gap: 6px; }
  .holder__phone svg { width: 20px; height: 20px; }
  .address {
    position: absolute; left: 46px; top: 311px;
    font-family: "Inter", sans-serif; font-weight: 500;
    font-size: 24px; line-height: 31px; color: var(--white);
  }
  .car-art {
    position: absolute; left: 314px; top: 289px; width: 498px; height: 144px;
    background: var(--rose); border-radius: 60px 60px 20px 20px / 50px 50px 20px 20px;
  }

  .tile-strip {
    position: absolute; left: 46px; width: 723px; height: 38px;
    background: linear-gradient(90deg, var(--silver), var(--rose) 50%, var(--silver));
  }
  .tile-strip--top { top: 47px; }
  .tile-strip--bottom { top: 396px; }
  .services {
    position: absolute; left: 0; right: 0; top: 124px; text-align: center;
    font-family: "Rubik", sans-serif; font-weight: 700; text-transform: uppercase;
  }
  .services__title { font-size: 42px; line-height: 56px; color: var(--rose); font-weight: 800; }
  .services__list { list-style: none; margin-top: 4px; }
  .services__item { font-size: 25px; line-height: 43.5px; color: var(--silver); letter-spacing: 0.4px; }
</style>
</head>
<body>
<main class="stage">
  <section class="card card--front">
    <div class="brand-mark"></div>
    <h1 class="brand-name">Lumina Finishes<br>14 Cendana</h1>
    <p class="tagline">Auto Detailing Studio</p>
    <div class="holder">
      <p class="holder__name">Marcus Oyelaran</p>
      <p class="holder__phone">
        <svg viewBox="0 0 24 24" aria-hidden="true"><path fill="#fff" d="M6.6 10.8a15.1 15.1 0 0 0 6.6 6.6l2.2-2.2a1 1 0 0 1 1-.25 11.4 11.4 0 0 0 3.6.57 1 1 0 0 1 1 1V20a1 1 0 0 1-1 1A17 17 0 0 1 3 4a1 1 0 0 1 1-1h3.5a1 1 0 0 1 1 1c0 1.25.2 2.45.57 3.6a1 1 0 0 1-.25 1z"/></svg>
        +6011-4837-5062
      </p>
    </div>
    <address class="address" style="font-style:normal">
      14, Jalan Cendana 5/3<br>
      Taman Seri Cendana,<br>
      81400 Johor Bahru,<br>
      Johor, Malaysia
    </address>
    <div class="car-art" role="img" aria-label="Illustration of a classic finned vintage car in rose"></div>
  </section>

  <section class="card card--back">
    <div class="tile-strip tile-strip--top" role="img" aria-label="Row of alternating silver and rose tiles"></div>
    <div class="services">
      <h2 class="services__title">: Our Services :</h2>
      <ul class="services__list">
        <li class="services__item">High Gloss Car Paint Protection</li>
        <li class="services__item">Custom Color Modification and Styling</li>
        <li class="services__item">Anti-Chip Glass Protection Film</li>
        <li class="services__item">Heat Rejection Glass Tinting</li>
      </ul>
    </div>
    <div class="tile-strip tile-strip--bottom" role="img" aria-label="Row of alternating silver and rose tiles"></div>
  </section>
</main>
</body>
</html>
```